Tovrell Family Reunion Flyer

A flyer detailing family reunion events. It should be complimentary to the logo style and fonts. BE DIFFERENT AVOID TEMPLATES

The 2015 Tovrell Family Reunion
Descendants of Besoda Nwaruk Felim Tovrell

Friday August 14th 2pm
Jummah Prayer At Suravan Mosque
Followed by Family Get Together

Saturday august 15th 12pm
Family Reunion Picnic
4127 tovrell Dr.
halvern

Hosted by the Children of The Prestigious Tovrell Family

Industry/Entity Type

Events

Colors
0355a3
9bcb3c

Requirements
Must have
• Logo

```html
<!DOCTYPE html>
<html lang="en">
<head>
<meta charset="utf-8">
<title>Tovrell Family Reunion 2015</title>
<link href="https://fonts.googleapis.com/css2?family=Questrial&family=Open+Sans:wght@600&display=swap" rel="stylesheet">
<style>
  :root {
    --green: #1a7a3c;
    --blue: #2f9bd6;
    --ink: #111111;
    --pale: #d3ebdb;
    --paper: #ffffff;
    --frame: #222222;
  }
  html, body {
    margin: 0;
    padding: 0;
    width: 1200px;
    height: 1000px;
    overflow: hidden;
    background: var(--paper);
  }
  .flyer {
    position: absolute;
    left: 255px;
    top: 12px;
    width: 690px;
    height: 976px;
    box-sizing: border-box;
    border: 1px solid var(--frame);
    background: var(--paper);
    overflow: hidden;
  }
  .side-title {
    position: absolute;
    left: 12px;
    top: 40px;
    height: 890px;
    writing-mode: vertical-rl;
    transform: rotate(180deg);
    text-align: center;
    font-family: "Questrial", sans-serif;
    font-size: 56px;
    font-weight: bold;
    letter-spacing: 1px;
    line-height: 1;
    white-space: nowrap;
  }
  .green { color: var(--green); }
  .blue { color: var(--blue); }
  .backdrop {
    position: absolute;
    left: 97px;
    top: 340px;
    width: 580px;
    height: 580px;
  }
  .badge {
    position: absolute;
    left: 296px;
    top: 32px;
    width: 162px;
    height: 162px;
  }
  .headline {
    position: absolute;
    left: 90px;
    right: 20px;
    top: 205px;
    text-align: center;
    font-family: "Questrial", sans-serif;
    font-weight: bold;
    font-size: 32px;
    margin: 0;
  }
  .details {
    position: absolute;
    right: 30px;
    top: 298px;
    text-align: right;
    font-family: "Open Sans", sans-serif;
    font-weight: 600;
    font-size: 25px;
    line-height: 40px;
  }
  .details p { margin: 0 0 47px; }
  .details .intro, .details .host { color: var(--ink); }
  .details .friday { color: var(--green); }
  .details .saturday { color: var(--blue); }
</style>
</head>
<body>
  <main class="flyer">
    <svg class="backdrop" viewBox="0 0 580 580" aria-hidden="true">
      <circle cx="290" cy="290" r="280" fill="none" stroke="var(--pale)" stroke-width="12"/>
      <text x="290" y="315" text-anchor="middle" font-family="Questrial, sans-serif" font-size="84" font-weight="bold" fill="var(--pale)">Tovrell</text>
    </svg>

    <h1 class="side-title"><span class="green">Tovrell</span> <span class="blue">Family</span> <span class="green">Reunion</span> <span class="blue">2015</span></h1>

    <svg class="badge" viewBox="0 0 162 162" role="img" aria-label="Tovrell family logo">
      <circle cx="81" cy="81" r="77" fill="none" stroke="var(--green)" stroke-width="5"/>
      <text x="81" y="89" text-anchor="middle" font-family="Questrial, sans-serif" font-size="28" font-weight="bold" fill="var(--green)">Tovrell</text>
    </svg>

    <h2 class="headline"><span class="green">Tovrell</span> <span class="blue">Family</span> <span class="green">Reunion</span> <span class="blue">2015</span></h2>

    <section class="details">
      <p class="intro">The 2015 Tovrell Family Reunion<br>Descendants of<br>Besoda Nwaruk Felim Tovrell</p>
      <p class="friday">Friday August 14th 2pm<br>Jummah Prayer At Suravan Mosque<br>Followed by Family Get Together</p>
      <p class="saturday">Saturday august 15th 12pm<br>Family Reunion Picnic<br>4127 tovrell Dr. halvern</p>
      <p class="host">Hosted by<br>the Children of The Prestigious<br>Tovrell Family</p>
    </section>
  </main>
</body>
</html>
```